Commercial Cleaning Company Needs A Flyer

We are a commercial cleaning company based in London.
We are currently trying to grow our client base and would like a fresh, professional flyer that differentiates us from the competition. We mainly specialises in commercial cleaning such as offices, educational facilities etc. I would like to see a flyer design that look professional, unique not cheap. I have attached a file that contains some company details but Im happy to explore other options if thay are relevant. Please also find company Brightway and colour chart, this should remain as is.

I have attached some pictures that contain diamond shaped windows. I feel that this can be used to represent and incorporate the Brightway. Please add to flyer where possible.

Please feel free to contact me for any further advice.
Thanks and good luck

Target Market(s)

commercial buildings and residential property owners

Industry/Entity Type

Cleaning Service

Contact Information for Business Card

Please refer to up loaded document for company details and Brightway colours.

Font styles to use
Sans Serif

Colors
33a6d7
33b8a4

Requirements
Must have
• Look Professional, not cheap, unique, stand out from others.

```html
<!DOCTYPE html>
<html lang="en">
<head>
<meta charset="utf-8">
<title>Cleaning Company Flyer</title>
<link rel="stylesheet" href="https://fonts.googleapis.com/css2?family=Russo+One&family=Roboto:wght@400;500;700&family=Quicksand:wght@500&display=swap">
<style>
:root{
  --navy:#2b2a9c;
  --teal:#1fb7a0;
  --teal-light:#45c6b2;
  --teal-pale:#6fd3c2;
  --white:#ffffff;
  --ink:#1d1d2b;
  --photo-a:#e9ebee;
  --photo-b:#b9c3cc;
  --stage:#eceef2;
}
*{margin:0;padding:0;box-sizing:border-box}
html,body{width:1041px;height:1200px;overflow:hidden;background:var(--stage)}
.flyer{
  position:absolute;left:110px;top:20px;width:765px;height:1081px;
  transform:scale(1.073);transform-origin:0 0;overflow:hidden;background:var(--teal);
  font-family:"Roboto",sans-serif;
}
.flyer-art{position:absolute;inset:0}
.brand-name{position:absolute;left:560px;top:38px;width:190px;text-align:right;font-family:"Roboto",sans-serif;font-weight:700;font-size:40px;color:var(--navy);letter-spacing:-1px}
.headline{position:absolute;top:496px;left:0;width:765px;text-align:center;font-family:"Russo One",sans-serif;font-size:26px;color:var(--navy);letter-spacing:.5px;-webkit-text-stroke:.6px var(--white)}
.intro{position:absolute;top:544px;left:0;width:765px;text-align:center;font-size:22px;color:var(--ink);letter-spacing:.4px}
.intro mark{background:var(--navy);color:var(--white);padding:0 4px;border-radius:4px}
.sector{position:absolute;top:700px;width:170px;text-align:center;color:var(--white);font-size:14px;letter-spacing:.3px}
.benefits-title{position:absolute;left:0;top:815px;width:346px;height:42px;background:var(--navy);border-radius:0 14px 14px 0;color:var(--white);font-family:"Russo One",sans-serif;font-size:21px;line-height:42px;padding-left:24px;letter-spacing:.6px}
.benefit-list{position:absolute;list-style:none;font-family:"Quicksand",sans-serif;font-size:12px;color:var(--ink)}
.benefit-list li{position:relative;padding-left:25px;height:26px;line-height:14px}
.benefit-list li::before{content:"";position:absolute;left:0;top:1px;width:10px;height:10px;border:1.5px solid var(--teal)}
.benefit-list li::after{content:"";position:absolute;left:3px;top:2px;width:4px;height:7px;border:solid var(--navy);border-width:0 2px 2px 0;transform:rotate(45deg)}
.benefit-list .tall{height:38px}
.call-pill{position:absolute;left:455px;top:977px;width:330px;height:62px;background:var(--navy);border-radius:34px 0 0 34px;color:var(--white);display:flex;align-items:center;padding-left:14px;font-family:"Russo One",sans-serif;font-size:21px}
.call-pill .divider{width:1px;height:38px;background:var(--white);margin:0 7px}
.footer-address{position:absolute;left:34px;top:1048px;color:var(--white);font-family:"Quicksand",sans-serif;font-size:13px;display:flex;align-items:center;gap:12px}
.footer-web{position:absolute;right:24px;top:1046px;color:var(--white);font-size:19px;letter-spacing:.5px}
</style>
</head>
<body>
<main class="flyer">
  <svg class="flyer-art" viewBox="0 0 765 1081" width="765" height="1081" xmlns="http://www.w3.org/2000/svg">
    <defs>
      <linearGradient id="photoTone" x1="0" y1="0" x2="0" y2="1">
        <stop offset="0" stop-color="var(--photo-a)"/><stop offset="1" stop-color="var(--photo-b)"/>
      </linearGradient>
      <linearGradient id="roundTone" x1="0" y1="0" x2="1" y2="1">
        <stop offset="0" stop-color="#d9dde2"/><stop offset="1" stop-color="#9aa6b0"/>
      </linearGradient>
    </defs>
    <rect class="hero-photo" x="0" y="0" width="765" height="480" fill="url(#photoTone)" role="img" aria-label="Photo of cleaners vacuuming and wiping desks in an office, with a bucket of cleaning supplies and a mop"/>
    <path class="hero-swoosh" d="M0 355 C150 425 400 468 765 458 L765 472 C400 484 150 448 0 398 Z" fill="var(--navy)"/>
    <path class="teal-field" d="M0 380 C150 445 400 478 765 468 L765 1081 L0 1081 Z" fill="var(--teal)"/>
    <polygon points="0,470 230,470 120,760 0,760" fill="var(--teal-light)" opacity=".45"/>
    <polygon points="300,520 520,470 640,760 380,760" fill="var(--teal-light)" opacity=".35"/>
    <polygon points="640,480 765,470 765,880 700,760" fill="var(--teal-pale)" opacity=".35"/>
    <circle class="round-photo" cx="667" cy="435" r="73" fill="url(#roundTone)" stroke="var(--white)" stroke-width="4" role="img" aria-label="Photo of a cleaner wiping a computer desk"/>
    <line x1="215" y1="600" x2="215" y2="692" stroke="var(--navy)" stroke-width="2"/>
    <line x1="374" y1="600" x2="374" y2="692" stroke="var(--navy)" stroke-width="2"/>
    <line x1="542" y1="600" x2="542" y2="692" stroke="var(--navy)" stroke-width="2"/>
    <g fill="none" stroke="var(--white)" stroke-width="2">
      <circle cx="124" cy="641" r="43"/><circle cx="292" cy="641" r="43"/>
      <circle cx="458" cy="641" r="43"/><circle cx="632" cy="641" r="43"/>
    </g>
    <g class="icon-office" fill="var(--white)">
      <rect x="104" y="622" width="24" height="38"/><rect x="128" y="632" width="18" height="28"/><rect x="98" y="636" width="8" height="24"/>
      <g fill="var(--teal)"><rect x="108" y="627" width="5" height="5"/><rect x="118" y="627" width="5" height="5"/><rect x="108" y="637" width="5" height="5"/><rect x="118" y="637" width="5" height="5"/><rect x="108" y="647" width="5" height="5"/><rect x="118" y="647" width="5" height="5"/><rect x="133" y="638" width="4" height="4"/><rect x="133" y="648" width="4" height="4"/></g>
    </g>
    <g class="icon-school" fill="none" stroke="var(--white)" stroke-width="2">
      <rect x="272" y="614" width="40" height="9"/><rect x="270" y="623" width="44" height="38"/>
      <path d="M285 661 V645 a7 7 0 0 1 14 0 V661"/><rect x="275" y="630" width="7" height="7"/><rect x="302" y="630" width="7" height="7"/>
    </g>
    <g class="icon-restaurant" fill="none" stroke="var(--white)" stroke-width="2">
      <path d="M436 628 h44 l-3 -10 h-38 z" fill="var(--white)"/><rect x="438" y="628" width="40" height="34"/>
      <rect x="443" y="640" width="10" height="22"/><rect x="458" y="638" width="16" height="12"/>
    </g>
    <g class="icon-bank" fill="var(--white)">
      <polygon points="632,614 656,628 608,628"/><rect x="610" y="631" width="44" height="4"/>
      <rect x="614" y="637" width="5" height="18"/><rect x="624" y="637" width="5" height="18"/><rect x="635" y="637" width="5" height="18"/><rect x="645" y="637" width="5" height="18"/>
      <rect x="608" y="657" width="48" height="5"/>
    </g>
    <path class="lower-band" d="M0 748 C220 710 520 745 765 872 L765 890 C520 765 220 728 0 768 Z" fill="var(--navy)"/>
    <path class="lower-panel" d="M0 760 C220 722 520 757 765 884 L765 1081 L0 1081 Z" fill="var(--white)"/>
    <rect x="0" y="1027" width="765" height="5" fill="var(--navy)"/>
    <rect class="footer-bar" x="0" y="1032" width="765" height="49" fill="var(--teal)"/>
  </svg>

  <div class="brand-name">Brightway</div>
  <h1 class="headline">CLEANING COMPANY</h1>
  <p class="intro">We mainly specialises in <mark>commercial cleaning</mark> such as</p>

  <span class="sector" style="left:39px">Office and Building</span>
  <span class="sector" style="left:207px">Educational</span>
  <span class="sector" style="left:373px">Restaurant</span>
  <span class="sector" style="left:547px">Bank</span>

  <h2 class="benefits-title">BENEFITS OF CLEANING</h2>
  <ul class="benefit-list" style="left:35px;top:884px">
    <li>Lorem Ipsum is simply dummy text</li>
    <li>of the printing and typesetting</li>
    <li>Lorem Ipsum has been the</li>
    <li>industry's standard dummy text ever</li>
  </ul>
  <ul class="benefit-list" style="left:272px;top:884px">
    <li>It is a long established fact that a reader</li>
    <li>Lorem Ipsum is that it has a</li>
    <li>Content here, content here'</li>
    <li>when looking at its layout</li>
  </ul>
  <ul class="benefit-list" style="left:540px;top:884px">
    <li class="tall">It is a long established fact that<br>a reader will be distracted by the</li>
    <li>readable content of a page</li>
    <li>established fact that a reader</li>
  </ul>

  <div class="call-pill"><span>CALL NOW</span><span class="divider"></span><span>123-456-789</span></div>

  <div class="footer-address">
    <svg width="10" height="14" viewBox="0 0 10 14"><path d="M5 0a5 5 0 0 1 5 5c0 4-5 9-5 9S0 9 0 5a5 5 0 0 1 5-5z" fill="var(--navy)"/><circle cx="5" cy="5" r="2" fill="var(--teal)"/></svg>
    <span>comes from a line in section 1.10.32.</span>
  </div>
  <div class="footer-web">www.brightwayclean.co.uk</div>
</main>
</body>
</html>
```